EB-5 Regional Center needs a Web design

Tallowmere Funding Partners is an expanding EB-r regional center. We have been successful in sponsoring multiple projects of third-party developers and placing EB-5, B-1, and Private Investments into multiple projects.

We are now partnering directly with project developers in the energy and healthcare to raise foreign capital for projects in those industries. The foreign capital is used as project equity and our collective balance sheets are used to guarantee debt to complete the funding of the projects.

We need a web site where we can post our company credentials, the bios of each partner, a document page for each of our projects where we can post specific project related documents which foreign investors can read, and we will need a section where foreign investors can fill out investor forms confirming that they are qualified investors and leaving their contact so that our agents and executives can make contact.

The final design should reflect the exceptional experience of the partners and our financial strength and stability.

We do have a logo we would want to use on the web design.

Target Market(s)

EB-5 Investors, B-1 Investors, Private Equity and other investors seeking quality investment in job creating US projects.

Coding

Number of Pages Required

5+ page

Font styles to use
Sans Serif

Requirements
Must have
• Pages to display company info, partner bios, projects completed, and a projects in-process page where we can post documents and info on projects for which we are seeking foreign investment. We also need a section where investors can enter their qualifying personal information and leave contact information for us.

```html
<!DOCTYPE html>
<html lang="en">
<head>
<meta charset="utf-8">
<title>Tallowmere Funding Partners</title>
<link href="https://fonts.googleapis.com/css2?family=Lato:wght@300;400;700&family=Montserrat:wght@400;500;600;700&display=swap" rel="stylesheet">
<style>
:root{
  --blue:#1a8fd1;
  --blue-light:#4aa9db;
  --ink:#3d4145;
  --text:#8d9196;
  --muted:#a4a8ad;
  --grey-band:#eeeff0;
  --rule:#e3e5e7;
  --footer:#393c41;
  --footer-text:#8b8e93;
  --white:#ffffff;
}
*{margin:0;padding:0;box-sizing:border-box}
html,body{width:1200px;height:4870px;overflow:hidden;background:var(--white)}
body{position:relative;font-family:"Montserrat",sans-serif;color:var(--text)}
.abs{position:absolute}
.heading{font-family:"Lato",sans-serif;font-weight:300;color:var(--ink)}
.lead{font-size:13.5px;line-height:22px;color:var(--muted);text-align:center}
.btn{position:absolute;display:flex;align-items:center;justify-content:center;background:var(--blue);color:var(--white);font-size:13px;font-weight:500;border-radius:24px}
.small{font-size:11.5px;line-height:18.5px;color:var(--muted)}

.hero{left:0;top:0;width:1200px;height:822px;background:linear-gradient(120deg,#c9d5e0 0%,#8ea1b4 35%,#4f6377 62%,#2f3d4c 100%)}
.nav{left:0;top:0;width:1200px;height:62px;background:rgba(40,48,58,.72)}
.brand{left:135px;top:12px;display:flex;align-items:center;gap:10px;color:var(--white)}
.brand-mark{width:30px;height:30px;border-radius:50%;background:#aeb6c0}
.brand-name{font-size:19px;font-weight:500;letter-spacing:1px;line-height:22px}
.brand-sub{font-size:7px;letter-spacing:2.4px;color:#c5ccd3}
.nav-links{left:544px;top:15px;display:flex;gap:23px;font-size:12px;font-weight:500;color:var(--white)}
.nav-links .on{color:#5ab7ea}
.side-tools{left:1147px;top:104px;width:53px}
.side-tools div{width:53px;height:52px;background:var(--blue);margin-bottom:3px;display:flex;align-items:center;justify-content:center}

.feature{width:270px}
.feature h3{font-family:"Lato",sans-serif;font-weight:400;font-size:19px;color:var(--ink);margin-left:52px;line-height:24px}
.feature p{margin:10px 0 0 52px;width:216px}
.feature svg{position:absolute;left:0;top:-6px}

.packages{left:0;top:1281px;width:1200px;height:706px;background:var(--grey-band)}
.card{top:1533px;width:275px;height:365px;color:var(--white);text-align:center}
.card h4{font-size:14px;font-weight:700;margin-top:30px}
.card hr{border:0;border-top:1px solid rgba(255,255,255,.6);width:193px;margin:18px auto 0}
.card .price{font-family:"Lato",sans-serif;font-weight:300;font-size:58px;margin-top:14px;line-height:70px}
.card p{font-size:11.5px;line-height:18.5px;width:220px;margin:14px auto 0;font-weight:500}
.card .outline{width:170px;height:48px;border:2px solid var(--white);border-radius:26px;margin:34px auto 0;display:flex;align-items:center;justify-content:center;font-size:13px;font-weight:500}

.exp{width:210px;text-align:center}
.exp h5{font-size:14px;font-weight:700;color:var(--ink);line-height:21px;margin-top:22px}
.exp p{margin-top:12px}
.exp a{display:block;margin-top:16px;font-size:12.5px;font-weight:600;color:var(--blue);text-decoration:none}
.vrule{width:1px;height:250px;background:var(--rule);top:2750px}
.col3 h6{font-family:"Lato",sans-serif;font-weight:400;font-size:18.5px;color:var(--ink)}
.col3 p{margin-top:14px;width:275px}

.about-photo{left:0;top:3449px;width:599px;height:397px;background:linear-gradient(135deg,#e7ebee 0%,#b7c1c9 45%,#6d7884 100%)}
.about-panel{left:599px;top:3449px;width:601px;height:397px;background:var(--blue)}
.bar-label{font-size:8.5px;font-weight:700;color:var(--white);display:flex;justify-content:space-between;width:372px}
.bar{width:372px;height:7px;background:rgba(255,255,255,.35);margin-top:4px;border-radius:4px}
.bar i{display:block;height:7px;background:var(--white);border-radius:4px}

.testi-band{left:0;top:3846px;width:1200px;height:637px;background:#f4f5f6}
.quote{top:4099px;width:267px;height:195px;background:var(--white);box-shadow:0 1px 6px rgba(0,0,0,.06)}
.quote::after{content:"";position:absolute;left:40px;bottom:-18px;border-left:18px solid var(--white);border-bottom:18px solid transparent}
.quote .mark{position:absolute;left:26px;top:20px;font-family:"Lato",sans-serif;font-weight:700;font-size:34px;color:var(--blue)}
.quote p{position:absolute;left:30px;top:58px;width:212px;font-size:11.5px;line-height:18.5px}
.person{top:4331px;display:flex;align-items:center;gap:16px}
.avatar{width:72px;height:72px;background:linear-gradient(160deg,#e4c9b4,#9aa6b3)}
.person b{display:block;font-weight:500;font-size:12.5px;color:var(--ink)}
.person span{font-size:8.5px;color:var(--blue);font-weight:600}

.footer{left:0;top:4483px;width:1200px;height:387px;background:var(--footer);color:var(--footer-text)}
.fcol{top:74px;font-size:11px;line-height:17px}
.fcol h6{font-family:"Lato",sans-serif;font-weight:400;font-size:18.5px;color:#d9dbde;margin-bottom:22px}
.fcol li{list-style:none;margin-bottom:15px}
.fcol em{font-style:normal;color:#6a6e74}
</style>
</head>
<body>

<div class="abs hero" role="img" aria-label="Photo of two partners reviewing project documents at a laptop"></div>
<header class="abs nav">
  <div class="abs brand">
    <div class="brand-mark"></div>
    <div><div class="brand-name">TALLOWMERE</div><div class="brand-sub">FUNDING PARTNERS</div></div>
  </div>
  <nav class="abs nav-links"><span class="on">Home</span><span>Company</span><span>Partners</span><span>Projects &amp; Documents</span><span>Investors</span><span>Contact</span></nav>
</header>
<div class="abs side-tools">
  <div><svg width="20" height="18" viewBox="0 0 20 18" fill="none" stroke="#fff" stroke-width="1.6"><path d="M1 2h3l3 10h10l2-7H5"/><circle cx="8" cy="15.5" r="1.5"/><circle cx="15" cy="15.5" r="1.5"/></svg></div>
  <div><svg width="20" height="18" viewBox="0 0 20 18" fill="none" stroke="#fff" stroke-width="1.6"><rect x="1" y="3" width="15" height="12" rx="1"/><path d="M4 1h15v12"/><path d="M4 8h9M4 11h6"/></svg></div>
  <div><svg width="20" height="16" viewBox="0 0 20 16" fill="none" stroke="#fff" stroke-width="1.6"><rect x="1" y="1" width="18" height="14" rx="1"/><path d="M1 5h18"/></svg></div>
</div>
<div class="btn" style="left:526px;top:555px;width:148px;height:42px">Invest Today!</div>

<section>
  <div class="abs feature" style="left:160px;top:899px">
    <svg width="40" height="36" viewBox="0 0 40 36" fill="none" stroke="var(--blue)" stroke-width="1.6"><ellipse cx="14" cy="8" rx="11" ry="4"/><path d="M3 8v6c0 2 5 4 11 4M3 14v6c0 2 5 4 9 4"/><circle cx="27" cy="24" r="9"/><path d="M27 19v10M24.5 21.5h4a2 2 0 010 4h-3a2 2 0 000 4h4"/></svg>
    <h3>EB-5 Sponsorship</h3>
    <p class="small">Regional center sponsorship for third-party developers, placing EB-5 capital into job creating US projects with full compliance.</p>
  </div>
  <div class="abs feature" style="left:463px;top:899px">
    <svg width="40" height="36" viewBox="0 0 40 36" fill="none" stroke="var(--blue)" stroke-width="1.6"><path d="M22 2L8 20h10l-4 14 16-20H20z"/></svg>
    <h3>Energy Projects</h3>
    <p class="small">Direct partnerships with energy developers, using foreign capital as project equity for new generation and storage sites.</p>
  </div>
  <div class="abs feature" style="left:762px;top:899px">
    <svg width="40" height="36" viewBox="0 0 40 36" fill="none" stroke="var(--blue)" stroke-width="1.6"><rect x="2" y="9" width="36" height="24" rx="2"/><path d="M14 9V4h12v5M2 18h36"/><rect x="17" y="15" width="6" height="6"/></svg>
    <h3>Private Investment</h3>
    <p class="small">B-1 and private equity placements alongside EB-5 funds, with debt guaranteed by our collective balance sheets.</p>
  </div>
  <div class="abs feature" style="left:160px;top:1069px">
    <svg width="40" height="36" viewBox="0 0 40 36" fill="none" stroke="var(--blue)" stroke-width="1.6"><path d="M6 4l6 0 3 7-4 3c2 5 5 8 10 10l3-4 7 3v6c-14 1-28-12-25-25z"/></svg>
    <h3>Investor Support</h3>
    <p class="small">Our agents and executives contact every qualified investor to guide documents, filings and the steps to petition.</p>
  </div>
  <div class="abs feature" style="left:463px;top:1069px">
    <svg width="40" height="36" viewBox="0 0 40 36" fill="none" stroke="var(--blue)" stroke-width="1.6"><rect x="4" y="4" width="32" height="28" rx="2"/><path d="M20 10v16M12 18h16"/></svg>
    <h3>Healthcare Projects</h3>
    <p class="small">Capital for hospitals, clinics and senior care facilities built by trusted developers in underserved US markets.</p>
  </div>
  <div class="abs feature" style="left:762px;top:1069px">
    <svg width="40" height="36" viewBox="0 0 40 36" fill="none" stroke="var(--blue)" stroke-width="1.6"><path d="M10 3h20v9a10 10 0 01-20 0z"/><path d="M10 6H3c0 6 3 9 7 9M30 6h7c0 6-3 9-7 9M20 22v6M13 33h14M15 28h10v5"/></svg>
    <h3>Proven Track Record</h3>
    <p class="small">Multiple funded projects, thousands of jobs created and a history of investors reaching their visa goals.</p>
  </div>
</section>

<section class="abs packages"></section>
<h2 class="abs heading" style="left:0;top:1348px;width:1200px;text-align:center;font-size:38px">Projects in Process</h2>
<p class="abs lead" style="left:260px;top:1406px;width:680px">Open offerings seeking foreign investment. Each project has its own document page with offering files, budgets and job creation reports.</p>
<div class="abs card" style="left:160px;background:var(--blue-light)">
  <h4>ENERGY PROJECT</h4><hr><div class="price">$800K</div>
  <p>Solar and battery storage site. Minimum EB-5 investment per investor in a targeted employment area</p>
  <div class="outline">View Documents</div>
</div>
<div class="abs card" style="left:463px;background:var(--blue)">
  <h4>HEALTHCARE PROJECT</h4><hr><div class="price">$1.05M</div>
  <p>Regional medical campus. Standard EB-5 investment with equity held in the project partnership</p>
  <div class="outline">View Documents</div>
</div>
<div class="abs card" style="left:765px;background:var(--blue-light)">
  <h4>PRIVATE PLACEMENT</h4><hr><div class="price">$250K</div>
  <p>B-1 and private equity tranche open to qualified investors seeking job creating US assets</p>
  <div class="outline">View Documents</div>
</div>

<div class="abs" style="left:147px;top:2060px;width:388px;height:444px;background:linear-gradient(180deg,#f3f6f8 0%,#c9dcec 55%,#9fbfdc 100%)" role="img" aria-label="Photo of a smiling investor advisor"></div>
<h2 class="abs heading" style="left:539px;top:2064px;width:500px;font-size:38px;line-height:46px">Become a Qualified Investor</h2>
<p class="abs" style="left:539px;top:2168px;width:500px;font-size:13px;line-height:23px;color:var(--muted)">Complete our investor form to confirm that you meet the qualifying standards for EB-5, B-1 or private investment. Share your country, investment range, source of funds and preferred contact details. Once reviewed, our agents and executives will contact you directly to share project documents and answer your questions.</p>
<div class="btn" style="left:539px;top:2357px;width:174px;height:48px">Investor Form</div>

<h2 class="abs heading" style="left:0;top:2572px;width:1200px;text-align:center;font-size:38px">Experience the Difference</h2>
<p class="abs lead" style="left:260px;top:2630px;width:680px">The exceptional experience of our partners and the strength of our balance sheets give investors stability from first filing to final return.</p>
<div class="abs vrule" style="left:374px"></div>
<div class="abs vrule" style="left:600px"></div>
<div class="abs vrule" style="left:826px"></div>
<div class="abs exp" style="left:156px;top:2750px">
  <svg width="64" height="62" viewBox="0 0 64 62" fill="none" stroke="var(--blue)" stroke-width="2"><rect x="10" y="4" width="44" height="54" rx="2"/><path d="M20 18h24M20 28h24M20 38h16"/><path d="M36 46l4 4 8-8"/></svg>
  <h5>COMPANY<br>CREDENTIALS</h5>
  <p class="small">Licensed regional center status, audited financials and compliance records available for review.</p>
  <a>Learn more</a>
</div>
<div class="abs exp" style="left:382px;top:2750px">
  <svg width="64" height="62" viewBox="0 0 64 62" fill="none" stroke="var(--blue)" stroke-width="2"><circle cx="24" cy="20" r="9"/><circle cx="44" cy="22" r="7"/><path d="M6 54c0-12 8-20 18-20s18 8 18 20M40 34c9 0 18 6 18 18"/></svg>
  <h5>PARTNER<br>BIOS</h5>
  <p class="small">Meet the partners behind every project, with decades in finance, development and law.</p>
  <a>Learn more</a>
</div>
<div class="abs exp" style="left:608px;top:2750px">
  <svg width="64" height="62" viewBox="0 0 64 62" fill="none" stroke="var(--blue)" stroke-width="2"><path d="M18 4h28v16a14 14 0 01-28 0z"/><path d="M18 8H6c0 10 5 15 12 15M46 8h12c0 10-5 15-12 15M32 34v12M22 58h20M24 46h16v12"/></svg>
  <h5>COMPLETED<br>PROJECTS</h5>
  <p class="small">A record of funded developments placing EB-5, B-1 and private capital into US jobs.</p>
  <a>Learn more</a>
</div>
<div class="abs exp" style="left:834px;top:2750px">
  <svg width="64" height="62" viewBox="0 0 64 62" fill="none" stroke="var(--blue)" stroke-width="2"><path d="M14 4h26l12 12v42H14z"/><path d="M40 4v12h12M22 30h22M22 40h22M22 50h14"/></svg>
  <h5>PROJECT<br>DOCUMENTS</h5>
  <p class="small">Offering memoranda, budgets and economic reports posted for each open project.</p>
  <a>Learn more</a>
</div>

<div class="abs" style="left:0;top:3118px;width:1200px;height:1px;background:var(--rule)"></div>
<div class="abs col3" style="left:160px;top:3198px">
  <h6>Managing Partner</h6>
  <p class="small">Ruth Calloway has led capital raising for regional centers for over twenty years, sponsoring projects across energy, hospitality and healthcare and placing investors from more than thirty countries.</p>
</div>
<div class="abs col3" style="left:463px;top:3198px">
  <h6>Development Partner</h6>
  <p class="small">Gordon Abernay oversees our direct partnerships with project developers, reviewing budgets, construction schedules and job creation models before any offering is opened to foreign investors.</p>
</div>
<div class="abs col3" style="left:764px;top:3198px">
  <h6>Finance Partner</h6>
  <p class="small">Irene Talbeck manages our balance sheet guarantees and debt placement, structuring each project so that foreign equity is protected and senior funding is secured to complete construction.</p>
</div>

<div class="abs about-photo" role="img" aria-label="Photo of partners meeting around a conference table"></div>
<div class="abs about-panel">
  <h2 class="abs heading" style="left:49px;top:44px;font-size:38px;color:var(--white)">About Us</h2>
  <p class="abs" style="left:49px;top:110px;width:360px;font-size:13.5px;line-height:24px;color:var(--white);font-weight:500">An expanding EB-5 regional center raising foreign capital for energy and healthcare projects</p>
  <div class="abs" style="left:49px;top:210px">
    <div class="bar-label"><span>PROJECTS FULLY FUNDED</span><span>98</span></div><div class="bar"><i style="width:98%"></i></div>
  </div>
  <div class="abs" style="left:49px;top:248px">
    <div class="bar-label"><span>CAPITAL DEPLOYED</span><span>66</span></div><div class="bar"><i style="width:66%"></i></div>
  </div>
  <div class="abs" style="left:49px;top:287px">
    <div class="bar-label"><span>PETITIONS APPROVED</span><span>87</span></div><div class="bar"><i style="width:87%"></i></div>
  </div>
</div>

<section class="abs testi-band"></section>
<h2 class="abs heading" style="left:0;top:3916px;width:1200px;text-align:center;font-size:38px">Testimonials</h2>
<p class="abs lead" style="left:260px;top:3974px;width:680px">Investors from around the world share their experience working with our partners, agents and executives through every project stage.</p>
<div class="abs quote" style="left:160px"><span class="mark">“</span><p>The project documents were clear and complete. My agent answered every question and guided me through the full EB-5 process with care.</p></div>
<div class="abs quote" style="left:469px"><span class="mark">“</span><p>Filling out the investor form took minutes, and an executive called me the next day. I felt confident in the strength of the partners.</p></div>
<div class="abs quote" style="left:746px"><span class="mark">“</span><p>Their healthcare project was well structured and the balance sheet guarantee gave my family real peace of mind about our investment.</p></div>
<div class="abs person" style="left:170px"><div class="avatar" role="img" aria-label="Investor portrait"></div><div><b>Dana Whitfield</b><span>SEATTLE</span></div></div>
<div class="abs person" style="left:463px"><div class="avatar" role="img" aria-label="Investor portrait"></div><div><b>Owen Castell</b><span>NEW YORK</span></div></div>
<div class="abs person" style="left:756px"><div class="avatar" role="img" aria-label="Investor portrait"></div><div><b>Lena Marsh</b><span>CHICAGO</span></div></div>

<footer class="abs footer">
  <div class="abs fcol" style="left:160px;width:200px;top:80px">
    <div style="display:flex;align-items:center;gap:8px;color:#e2e4e6;font-size:12px;font-weight:500;margin-bottom:28px"><span style="width:12px;height:12px;background:#d9dbde;display:inline-block"></span>Tallowmere Funding</div>
    <p>An EB-5 regional center placing foreign capital into job creating US projects in energy and healthcare.</p>
    <p style="margin-top:20px">All offerings are made only to qualified investors through official project documents.</p>
  </div>
  <div class="abs fcol" style="left:387px">
    <h6>Links</h6>
    <ul><li>Company Credentials</li><li>Partner Bios</li><li>Completed Projects</li><li>Projects in Process</li><li>Project Documents</li><li>Investor Form</li></ul>
  </div>
  <div class="abs fcol" style="left:613px;width:200px">
    <h6>Recent Projects</h6>
    <p>Project feed will update as new offerings open.</p>
  </div>
  <div class="abs fcol" style="left:839px;width:210px">
    <h6>Recent Comments</h6>
    <ul><li>Marcus Ellery <em>on</em> Energy Update</li><li>Peter Ashdown <em>on</em> Energy Update</li><li>Carlos Venn <em>on</em> Clinic Report</li><li>Hugh Barrow <em>on</em> Clinic Report</li></ul>
  </div>
</footer>

</body>
</html>
```